Rework of Honey Labels - Updated for clarity

I am looking for a re-do of our current creamed honey labels.
Creamed honey is a butter-consistency. There are 5 flavors - original, lavender, chocolate, lemon, cinnamon. We want for it to look sophisticated and luxurious. We want the labels to all be cohesive in this group, but to be able to easily tell the difference between the products by color or something quick besides just words to tell the difference in the product. The product will be an off-white/light amber - except for the chocolate which is the color of Cremoso. There are three size containers for each of these honeys. But we can just focus on the single size for this contest.
The honey market in our area is extremely competitive. Right now, I feel our labels look more homemade. I want something that stands out. We charge a premium for our products. We want for our labels to look like we are a superior product. We are getting our product in many local stores and need to differentiate ourselves. I am attaching some of the labels that I think stand out. As for the labels themselves. They can include that whole blurb about us as Brookvale Meadow - or not. It is not truly necessary to have on the labels. But the logo needs to be included.
For all of these, we want something unique and special. Like you are going for an English mid-day tea at an upscale hotel in London with the Queen (well, I guess now the King...but really I think of the Queen).
I am uploading our current labels and then a few labels to take inspiration from.
Updates
I just reworked the description to be more limited in what I was asking for. Looking for a label for creamed honey in one size jar only. Thank you.

```html
<!DOCTYPE html>
<html lang="en">
<head>
<meta charset="utf-8">
<title>Creamed Honey Labels</title>
<link rel="stylesheet" href="https://fonts.googleapis.com/css2?family=Montserrat:wght@400;500;600&family=Courgette&display=swap">
<style>
  :root {
    --paper: #ffffff;
    --label-cream: #f5f1ec;
    --ink: #1f1b18;
    --brand-green: #2f7d4f;
    --lavender: #8a4a9e;
    --cinnamon: #6a4114;
    --rule-grey: #8f8a80;
  }
  html, body {
    margin: 0;
    padding: 0;
    overflow: hidden;
    background: var(--paper);
  }
  .canvas {
    width: 1200px;
    height: 1038px;
    position: relative;
    overflow: hidden;
    background: var(--paper);
  }
  .labels { display: block; }
  .pure-mark, .net-weight {
    font-family: "Montserrat", sans-serif;
    font-weight: 500;
    font-size: 15px;
    letter-spacing: 2px;
    fill: var(--ink);
  }
  .brand-name {
    font-family: "Montserrat", sans-serif;
    font-weight: 600;
    font-size: 24px;
    fill: var(--brand-green);
  }
  .product-name {
    font-family: "Montserrat", sans-serif;
    font-weight: 500;
    font-size: 33px;
    letter-spacing: 2px;
    fill: var(--ink);
  }
  .flavor-name {
    font-family: "Courgette", cursive;
    font-size: 28px;
  }
  .lavender .band, .lavender .ring, .lavender .flavor-icon { fill: var(--lavender); }
  .lavender .flavor-name { fill: var(--lavender); }
  .lavender .inner-line { stroke: var(--lavender); }
  .cinnamon .band, .cinnamon .ring, .cinnamon .flavor-icon { fill: var(--cinnamon); }
  .cinnamon .flavor-name { fill: var(--cinnamon); }
  .cinnamon .inner-line { stroke: var(--cinnamon); }
  .strip-line { stroke: var(--label-cream); stroke-width: 2; }
  .rule { stroke: var(--rule-grey); stroke-width: 1.5; }
</style>
</head>
<body>
<div class="canvas">
  <svg class="labels" width="1200" height="1038" viewBox="0 0 1200 1038" xmlns="http://www.w3.org/2000/svg">
    <defs>
      <path id="arc-top" d="M 100 250 A 120 120 0 0 1 340 250"/>
      <path id="arc-bottom" d="M 92 510 A 128 128 0 0 0 348 510"/>
    </defs>

    <g class="label lavender" transform="translate(110,150)">
      <rect class="band" x="0" y="300" width="440" height="260"/>
      <rect class="band" x="150" y="0" width="100" height="120"/>
      <line class="strip-line" x1="175" y1="0" x2="175" y2="110"/>
      <rect x="64" y="94" width="312" height="572" rx="156" fill="var(--label-cream)"/>
      <rect class="ring" x="70" y="100" width="300" height="560" rx="150"/>
      <rect x="86" y="116" width="268" height="528" rx="134" fill="var(--label-cream)"/>
      <rect class="inner-line" x="110" y="140" width="220" height="480" rx="110" fill="none" stroke-width="1"/>
      <text class="pure-mark"><textPath href="#arc-top" startOffset="50%" text-anchor="middle">100 % PURE</textPath></text>
      <circle cx="220" cy="245" r="10" fill="var(--brand-green)"/>
      <text class="brand-name" x="220" y="300" text-anchor="middle">Brookvale</text>
      <text class="brand-name" x="220" y="331" text-anchor="middle">Meadow</text>
      <line class="rule" x1="140" y1="358" x2="300" y2="358"/>
      <text class="product-name" x="220" y="402" text-anchor="middle">CREAMED</text>
      <text class="product-name" x="220" y="444" text-anchor="middle">HONEY</text>
      <circle class="flavor-icon" cx="220" cy="505" r="30" role="img" aria-label="Lavender sprig emblem"/>
      <text class="flavor-name" x="220" y="578" text-anchor="middle">Lavender</text>
      <text class="net-weight"><textPath href="#arc-bottom" startOffset="50%" text-anchor="middle">LOREM IPSUM NET WT XX OZ</textPath></text>
    </g>

    <g class="label cinnamon" transform="translate(650,240)">
      <rect class="band" x="0" y="300" width="440" height="260"/>
      <rect class="band" x="170" y="0" width="100" height="120"/>
      <line class="strip-line" x1="195" y1="0" x2="195" y2="110"/>
      <line class="strip-line" x1="245" y1="0" x2="245" y2="110"/>
      <rect x="64" y="94" width="312" height="572" rx="156" fill="var(--label-cream)"/>
      <rect class="ring" x="70" y="100" width="300" height="560" rx="150"/>
      <rect x="86" y="116" width="268" height="528" rx="134" fill="var(--label-cream)"/>
      <rect class="inner-line" x="110" y="140" width="220" height="480" rx="110" fill="none" stroke-width="1"/>
      <text class="pure-mark"><textPath href="#arc-top" startOffset="50%" text-anchor="middle">100 % PURE</textPath></text>
      <circle cx="220" cy="245" r="10" fill="var(--brand-green)"/>
      <text class="brand-name" x="220" y="300" text-anchor="middle">Brookvale</text>
      <text class="brand-name" x="220" y="331" text-anchor="middle">Meadow</text>
      <line class="rule" x1="140" y1="358" x2="300" y2="358"/>
      <text class="product-name" x="220" y="402" text-anchor="middle">CREAMED</text>
      <text class="product-name" x="220" y="444" text-anchor="middle">HONEY</text>
      <circle class="flavor-icon" cx="220" cy="505" r="30" role="img" aria-label="Star anise spice emblem"/>
      <text class="flavor-name" x="220" y="578" text-anchor="middle">Cinnamon</text>
      <text class="net-weight"><textPath href="#arc-bottom" startOffset="50%" text-anchor="middle">LOREM IPSUM NET WT XX OZ</textPath></text>
    </g>
  </svg>
</div>
</body>
</html>
```